brisk-vale.com Real Estate, Investment, Financial corporate

Real Estate, Investment, Financial corporate looking site. Show present a professional firm, with an elegant display. Please see the attached file which includes the logo, palette and fonts.
Updates

We just starting the brief today. ( logo was delayed)

Target Market(s)

Investors, Corporate , B2b

Industry/Entity Type

real-estate investments

Number of Pages Required

3 page

Requirements
Must have
• Dazzling Homepage
Nice to have
• paralex

```html
<!DOCTYPE html>
<html lang="en">
<head>
<meta charset="utf-8">
<title>Brisk Vale Group — Real Estate</title>
<link href="https://fonts.googleapis.com/css2?family=Montserrat:wght@400;500;600;700;800&display=swap" rel="stylesheet">
<style>
:root{
  --gold:#c9950b;
  --gold-soft:#e1b867;
  --ink:#2b2b2b;
  --muted:#6b6b6b;
  --field:#f1f1f1;
  --dark:#333333;
  --white:#ffffff;
}
*{margin:0;padding:0;box-sizing:border-box}
html,body{width:739px;height:1200px;overflow:hidden;background:var(--white)}
body{position:relative;font-family:"Montserrat",sans-serif;color:var(--ink)}
.btn{position:absolute;background:var(--gold);color:var(--white);font-weight:700;border-radius:3px;display:flex;align-items:center;justify-content:center;text-transform:uppercase;letter-spacing:.1px}

/* header */
.site-header{position:absolute;left:0;top:0;width:739px;height:31px;background:var(--white)}
.brand{position:absolute;display:flex;align-items:center;gap:4px}
.brand-mark{border:1px solid currentColor;display:block}
.brand-name{font-weight:400;line-height:1}
.site-header .brand{left:138px;top:8px;color:var(--gold-soft)}
.site-header .brand-mark{width:15px;height:15px}
.site-header .brand-name{font-size:10px}
.nav a{position:absolute;top:13px;font-size:4.8px;font-weight:600;color:var(--ink);text-decoration:none}
.nav a.active{color:var(--gold)}
.nav-underline{position:absolute;left:391px;top:29px;width:27px;height:2px;background:var(--gold)}

/* hero */
.hero{position:absolute;left:0;top:31px;width:739px;height:269px;
  background:linear-gradient(100deg,#8a6c4a 0%,#a6875f 45%,#6a7258 75%,#4e6540 100%)}
.hero h1{position:absolute;left:138px;top:73px;width:250px;font-size:20px;line-height:19px;font-weight:800;color:var(--white)}
.hero p{position:absolute;left:138px;top:121px;width:250px;font-size:6.4px;line-height:9.4px;font-weight:700;color:var(--white)}
.hero .btn{left:138px;top:145px;width:58px;height:15px;font-size:4.6px}
.dots{position:absolute;display:flex;gap:2px}
.dots i{width:3px;height:3px;border-radius:50%;border:.6px solid var(--white);display:block}
.dots i.on{background:var(--white)}
.hero .dots{left:360px;top:215px}

/* search */
.search{position:absolute;left:202px;top:285px;width:335px;height:31px;background:var(--white);border-radius:3px;box-shadow:0 1px 4px rgba(0,0,0,.18)}
.field{position:absolute;top:8px;height:15px;background:var(--field);border-radius:2px;font-size:4.8px;color:#a9a9a9;padding-left:4px;display:flex;align-items:center}
.field svg{position:absolute;right:4px;top:5px}
.search .btn{left:269px;top:8px;width:58px;height:15px;font-size:4.6px}

.section-title{position:absolute;left:0;width:739px;text-align:center;font-size:12.5px;font-weight:700;color:var(--gold)}

/* property cards */
.card{position:absolute;width:147px;height:192px;background:var(--white);box-shadow:0 1px 3px rgba(0,0,0,.16)}
.card-photo{position:absolute;left:0;top:0;width:147px;height:123px}
.badge{position:absolute;left:101px;top:9px;width:39px;height:15px;background:var(--dark);border-radius:3px;color:var(--white);font-size:5px;font-weight:700;display:flex;align-items:center;justify-content:center}
.card h3{position:absolute;left:16px;top:131px;font-size:5px;font-weight:600;color:var(--ink)}
.specs{position:absolute;left:16px;top:149px;width:120px;display:flex;justify-content:space-between;font-size:4.8px;color:var(--muted)}
.specs span{display:flex;align-items:center;gap:3px}
.price{position:absolute;left:16px;top:169px;font-size:9.6px;font-weight:600;color:var(--ink)}
.card .btn{left:77px;top:168px;width:58px;height:15px;font-size:4.6px}

/* exclusive band */
.exclusive{position:absolute;left:0;top:791px;width:739px;height:105px;
  background:linear-gradient(90deg,#262b24 0%,#3a3530 50%,#2b2f28 100%)}
.exclusive h2{position:absolute;left:0;top:18px;width:739px;text-align:center;font-size:12.5px;font-weight:700;color:var(--white)}
.exclusive p{position:absolute;left:234px;top:37px;width:271px;text-align:center;font-size:5.3px;line-height:7.8px;color:var(--white)}
.exclusive .btn{left:331px;top:70px;width:77px;height:15px;font-size:4.6px}

/* testimonial */
.testimonial{position:absolute;left:167px;top:948px;width:405px;height:89px;background:var(--white);box-shadow:0 1px 3px rgba(0,0,0,.16)}
.avatar{position:absolute;left:15px;top:9px;width:72px;height:72px;border-radius:50%;background:#c8b8aa}
.testimonial h4{position:absolute;left:120px;top:28px;font-size:6.2px;font-weight:600;color:var(--ink)}
.testimonial p{position:absolute;left:120px;top:40px;width:270px;font-size:4.9px;line-height:7.5px;color:var(--muted)}
.arrow{position:absolute;top:986px}
.clients-dots{left:362px;top:1056px}
.clients-dots i{border-color:var(--gold)}
.clients-dots i.on{background:var(--gold)}

/* footer */
.site-footer{position:absolute;left:0;top:1079px;width:739px;height:121px;background:var(--dark);color:var(--white)}
.site-footer .brand{left:138px;top:18px;color:var(--white)}
.site-footer .brand-mark{width:20px;height:20px}
.site-footer .brand-name{font-size:12.5px}
.footer-about{position:absolute;left:138px;top:52px;width:170px;font-size:5.1px;line-height:7.7px}
.social{position:absolute;left:138px;top:83px;display:flex;gap:11px}
.social span{width:20px;height:20px;border-radius:50%;background:var(--white);display:block}
.footer-heading{position:absolute;top:22px;font-size:5px;font-weight:700}
.quick-links{position:absolute;left:347px;top:38px;list-style:none;font-size:5px;line-height:11.6px}
.newsletter-text{position:absolute;left:447px;top:39px;width:155px;font-size:5px;line-height:7.7px}
.newsletter-input{position:absolute;left:447px;top:62px;width:107px;height:15px;background:var(--white);border-radius:3px 0 0 3px}
.newsletter-btn{position:absolute;left:554px;top:62px;width:46px;height:15px;background:var(--gold);border-radius:0 3px 3px 0;font-size:4.8px;font-weight:700;display:flex;align-items:center;justify-content:center}
</style>
</head>
<body>

<header class="site-header">
  <div class="brand"><span class="brand-mark"></span><span class="brand-name">Brisk Vale</span></div>
  <nav class="nav">
    <a class="active" style="left:397px">HOME</a>
    <a style="left:440px">PROPERTIES</a>
    <a style="left:498px">ABOUT US</a>
  </nav>
  <div class="nav-underline"></div>
  <div class="btn" style="left:543px;top:8px;width:57px;height:15px;font-size:4.6px">Contact us</div>
</header>

<section class="hero" role="img" aria-label="Luxury villa terrace with pool at sunset">
  <h1>LOREM IMPSUM DOLOR SIT AMET</h1>
  <p>LOREM IPSUM DOLOR SIT AMET, CONSECTETUR ADIPISCING ELIT. DONEC BLANDIT LACUS QUIS HENDRERIT IACULIS.</p>
  <div class="btn">View property</div>
  <div class="dots"><i class="on"></i><i></i><i></i><i></i></div>
</section>

<form class="search">
  <div class="field" style="left:8px;width:77px">All Locations<svg width="6" height="4" viewBox="0 0 6 4"><path d="M.5.5 3 3 5.5.5" fill="none" stroke="#888" stroke-width=".8"/></svg></div>
  <div class="field" style="left:89px;width:77px">All Property Tipes<svg width="6" height="4" viewBox="0 0 6 4"><path d="M.5.5 3 3 5.5.5" fill="none" stroke="#888" stroke-width=".8"/></svg></div>
  <div class="field" style="left:170px;width:46px">Rooms<svg width="6" height="4" viewBox="0 0 6 4"><path d="M.5.5 3 3 5.5.5" fill="none" stroke="#888" stroke-width=".8"/></svg></div>
  <div class="field" style="left:220px;width:46px">Baths<svg width="6" height="4" viewBox="0 0 6 4"><path d="M.5.5 3 3 5.5.5" fill="none" stroke="#888" stroke-width=".8"/></svg></div>
  <div class="btn">Search</div>
</form>

<h2 class="section-title" style="top:334px">OUR LATEST PROPERTIES</h2>

<article class="card" style="left:138px;top:370px">
  <div class="card-photo" role="img" aria-label="Wooden country house on a lawn" style="background:linear-gradient(180deg,#b49a9a,#6d7a45)"></div>
  <div class="badge">Dallas, TX</div>
  <h3>LOREM IPSUM DOLOR SIT AMET</h3>
  <div class="specs">
    <span><svg width="5" height="7" viewBox="0 0 5 7"><path d="M.5.5h4v2h-4zM1 2.5 1.5 6.5h2L4 2.5" fill="none" stroke="#555" stroke-width=".6"/></svg>2 Baths</span>
    <span><svg width="10" height="7" viewBox="0 0 10 7"><path d="M1 6.5V1h8v5.5M.5 4h9M2 3h2.5M5.5 3H8" fill="none" stroke="#555" stroke-width=".6"/></svg>2 Rooms</span>
    <span><svg width="8" height="7" viewBox="0 0 8 7"><path d="M.5 6.5V2L4 .5 7.5 2v4.5M2 6.5V4h4v2.5" fill="none" stroke="#555" stroke-width=".6"/></svg>2 Cars</span>
  </div>
  <div class="price">$ 1,550</div>
  <div class="btn">View more</div>
</article>

<article class="card" style="left:296px;top:370px">
  <div class="card-photo" role="img" aria-label="Modern green two-storey house at dusk" style="background:linear-gradient(180deg,#7d8a80,#535d4c)"></div>
  <div class="badge">Dallas, TX</div>
  <h3>LOREM IPSUM DOLOR SIT AMET</h3>
  <div class="specs">
    <span><svg width="5" height="7" viewBox="0 0 5 7"><path d="M.5.5h4v2h-4zM1 2.5 1.5 6.5h2L4 2.5" fill="none" stroke="#555" stroke-width=".6"/></svg>2 Baths</span>
    <span><svg width="10" height="7" viewBox="0 0 10 7"><path d="M1 6.5V1h8v5.5M.5 4h9M2 3h2.5M5.5 3H8" fill="none" stroke="#555" stroke-width=".6"/></svg>2 Rooms</span>
    <span><svg width="8" height="7" viewBox="0 0 8 7"><path d="M.5 6.5V2L4 .5 7.5 2v4.5M2 6.5V4h4v2.5" fill="none" stroke="#555" stroke-width=".6"/></svg>2 Cars</span>
  </div>
  <div class="price">$ 1,550</div>
  <div class="btn">View more</div>
</article>

<article class="card" style="left:454px;top:370px">
  <div class="card-photo" role="img" aria-label="Dark clad modern building under a blue sky" style="background:linear-gradient(180deg,#2f4f9c,#3c4253)"></div>
  <div class="badge">Dallas, TX</div>
  <h3>LOREM IPSUM DOLOR SIT AMET</h3>
  <div class="specs">
    <span><svg width="5" height="7" viewBox="0 0 5 7"><path d="M.5.5h4v2h-4zM1 2.5 1.5 6.5h2L4 2.5" fill="none" stroke="#555" stroke-width=".6"/></svg>2 Baths</span>
    <span><svg width="10" height="7" viewBox="0 0 10 7"><path d="M1 6.5V1h8v5.5M.5 4h9M2 3h2.5M5.5 3H8" fill="none" stroke="#555" stroke-width=".6"/></svg>2 Rooms</span>
    <span><svg width="8" height="7" viewBox="0 0 8 7"><path d="M.5 6.5V2L4 .5 7.5 2v4.5M2 6.5V4h4v2.5" fill="none" stroke="#555" stroke-width=".6"/></svg>2 Cars</span>
  </div>
  <div class="price">$ 1,550</div>
  <div class="btn">View more</div>
</article>

<article class="card" style="left:138px;top:576px">
  <div class="card-photo" role="img" aria-label="Bright living room with sofas" style="background:linear-gradient(180deg,#e8e4dd,#cfc4b3)"></div>
  <div class="badge">Dallas, TX</div>
  <h3>LOREM IPSUM DOLOR SIT AMET</h3>
  <div class="specs">
    <span><svg width="5" height="7" viewBox="0 0 5 7"><path d="M.5.5h4v2h-4zM1 2.5 1.5 6.5h2L4 2.5" fill="none" stroke="#555" stroke-width=".6"/></svg>2 Baths</span>
    <span><svg width="10" height="7" viewBox="0 0 10 7"><path d="M1 6.5V1h8v5.5M.5 4h9M2 3h2.5M5.5 3H8" fill="none" stroke="#555" stroke-width=".6"/></svg>2 Rooms</span>
    <span><svg width="8" height="7" viewBox="0 0 8 7"><path d="M.5 6.5V2L4 .5 7.5 2v4.5M2 6.5V4h4v2.5" fill="none" stroke="#555" stroke-width=".6"/></svg>2 Cars</span>
  </div>
  <div class="price">$ 1,550</div>
  <div class="btn">View more</div>
</article>

<article class="card" style="left:296px;top:576px">
  <div class="card-photo" role="img" aria-label="Suburban brick house with lawn" style="background:linear-gradient(180deg,#9fb0c4,#6f8a48)"></div>
  <div class="badge">Dallas, TX</div>
  <h3>LOREM IPSUM DOLOR SIT AMET</h3>
  <div class="specs">
    <span><svg width="5" height="7" viewBox="0 0 5 7"><path d="M.5.5h4v2h-4zM1 2.5 1.5 6.5h2L4 2.5" fill="none" stroke="#555" stroke-width=".6"/></svg>2 Baths</span>
    <span><svg width="10" height="7" viewBox="0 0 10 7"><path d="M1 6.5V1h8v5.5M.5 4h9M2 3h2.5M5.5 3H8" fill="none" stroke="#555" stroke-width=".6"/></svg>2 Rooms</span>
    <span><svg width="8" height="7" viewBox="0 0 8 7"><path d="M.5 6.5V2L4 .5 7.5 2v4.5M2 6.5V4h4v2.5" fill="none" stroke="#555" stroke-width=".6"/></svg>2 Cars</span>
  </div>
  <div class="price">$ 1,550</div>
  <div class="btn">View more</div>
</article>

<article class="card" style="left:454px;top:576px">
  <div class="card-photo" role="img" aria-label="White cottage with picket fence in autumn" style="background:linear-gradient(180deg,#c2b38a,#a8976a)"></div>
  <div class="badge">Dallas, TX</div>
  <h3>LOREM IPSUM DOLOR SIT AMET</h3>
  <div class="specs">
    <span><svg width="5" height="7" viewBox="0 0 5 7"><path d="M.5.5h4v2h-4zM1 2.5 1.5 6.5h2L4 2.5" fill="none" stroke="#555" stroke-width=".6"/></svg>2 Baths</span>
    <span><svg width="10" height="7" viewBox="0 0 10 7"><path d="M1 6.5V1h8v5.5M.5 4h9M2 3h2.5M5.5 3H8" fill="none" stroke="#555" stroke-width=".6"/></svg>2 Rooms</span>
    <span><svg width="8" height="7" viewBox="0 0 8 7"><path d="M.5 6.5V2L4 .5 7.5 2v4.5M2 6.5V4h4v2.5" fill="none" stroke="#555" stroke-width=".6"/></svg>2 Cars</span>
  </div>
  <div class="price">$ 1,550</div>
  <div class="btn">View more</div>
</article>

<section class="exclusive" role="img" aria-label="Modern timber house among trees at evening">
  <h2>THE MOST EXCLUSIVE PROPERTIES</h2>
  <p>Lorem ipsum dolor sit amet, consectetur adipiscing elit. Aliquam neque odio, scelerisque eget lorem eu, sollicitudin efficitur neque. Ut varius vestibulum consequat. Donec placerat dapibus neque, a rutrum erat pretium eu.</p>
  <div class="btn">Contact us</div>
</section>

<h2 class="section-title" style="top:914px">WHAT CLIENTS SAY</h2>

<svg class="arrow" style="left:139px" width="7" height="13" viewBox="0 0 7 13"><path d="M6 1 1 6.5 6 12" fill="none" stroke="#777" stroke-width="1.2"/></svg>
<div class="testimonial">
  <div class="avatar" role="img" aria-label="Client portrait"></div>
  <h4>Lorem ipsum dolor sit amet</h4>
  <p>Lorem ipsum dolor sit amet, consectetur adipiscing elit. Aliquam neque odio, scelerisque eget lorem eu, sollicitudin efficitur neque. Ut varius vestibulum consequat. Donec placerat dapibus neque, a rutrum erat pretium eu.</p>
</div>
<svg class="arrow" style="left:593px" width="7" height="13" viewBox="0 0 7 13"><path d="M1 1 6 6.5 1 12" fill="none" stroke="#777" stroke-width="1.2"/></svg>
<div class="dots clients-dots"><i class="on"></i><i></i><i></i><i></i></div>

<footer class="site-footer">
  <div class="brand"><span class="brand-mark"></span><span class="brand-name">Brisk Vale</span></div>
  <p class="footer-about">Lorem ipsum dolor sit amet, consectetur adipiscing elit. Aliquam neque odio, scelerisque eget lorem eu, sollicitudin efficitur neque. Ut varius vestibulum consequat.</p>
  <div class="social" aria-label="Social links"><span></span><span></span><span></span><span></span></div>

  <div class="footer-heading" style="left:347px">QUICK LINKS</div>
  <ul class="quick-links">
    <li>About Us</li><li>Properties</li><li>Privacy Policy</li><li>Terms &amp; Conditions</li>
  </ul>

  <div class="footer-heading" style="left:447px">SUBSCRIBE TO OUR NEWSLETTER</div>
  <p class="newsletter-text">Lorem ipsum dolor sit amet, consectetur adipiscing elit. Aliquam neque odio, scelerisque eget lorem eu, sollicitudin.</p>
  <div class="newsletter-input"></div>
  <div class="newsletter-btn">SUBSCRIBE</div>
</footer>

</body>
</html>
```